Startup company business card (Media & Advertising)

we need a business card design for a company that is a startup in the media and aggregation industry. Card needs to look funky and of a new breed/modern and upmarket.

Target Market(s)

advertisers/ brand agencies & media publishers

Industry/Entity Type

Advertising

Contact Information for Business Card

Please ensure the front face signifies our brand (plumvexo.com) and back has details for the contact. Standard contact such as phone , address, email , website etc.

Font styles to use
Other font styles liked:
• use styleguide and logo font and color

Colors

Designer to choose colors to be used in the design.

Requirements
Must have
• We are disrupting the media and agency industry so subtlety would be good to use imagery to signify this
Nice to have
• Please use logo colors for branding
Should not have
• be as creative and provide few options. Pick a brand color from logo and styleguide

```html
<!DOCTYPE html>
<html lang="en">
<head>
<meta charset="utf-8">
<title>plumvexo business card</title>
<link rel="stylesheet" href="https://fonts.googleapis.com/css2?family=Arvo:wght@400;700&family=Mulish:wght@400;500&display=swap">
<style>
  :root {
    --page: #c4c4c4;
    --paper: #f1f1f1;
    --brand-red: #e0393f;
    --brand-red-deep: #a4213b;
    --ink: #161616;
    --card-dark: #221f20;
    --map-tone: #3d3a3b;
    --on-red: #ffffff;
  }
  * { box-sizing: border-box; margin: 0; padding: 0; }
  html, body {
    width: 1200px; height: 1200px; overflow: hidden;
    background: var(--page);
  }
  .card {
    position: absolute; left: 232px; width: 736px; height: 424px;
    border-radius: 40px; overflow: hidden;
  }
  .card--front { top: 106px; background: var(--paper); }
  .card--back { top: 662px; background: var(--card-dark); }

  .wordmark {
    position: absolute; display: flex; align-items: center; gap: 22px;
    font-family: "Arvo", serif; font-weight: 700; letter-spacing: 0.5px;
    z-index: 2;
  }
  .wordmark__dot { border-radius: 50%; background: var(--brand-red); flex: none; }
  .card--front .wordmark { left: 78px; top: 58px; font-size: 46px; color: var(--ink); }
  .card--front .wordmark__dot { width: 60px; height: 60px; }

  .contact-band {
    position: absolute; left: 0; top: 174px; width: 100%; height: 250px;
    background: linear-gradient(180deg, var(--brand-red-deep) 0%, var(--brand-red) 100%);
    color: var(--on-red);
    font-family: "Mulish", sans-serif;
    padding: 26px 0 0 78px;
  }
  .contact-band__name { font-family: "Arvo", serif; font-weight: 700; font-size: 23px; line-height: 1.1; }
  .contact-band__role { font-size: 17px; margin-top: 2px; }
  .contact-list { list-style: none; margin-top: 24px; font-size: 17px; line-height: 21.5px; }
  .contact-list li { display: flex; align-items: center; gap: 10px; }
  .contact-list svg { width: 15px; height: 15px; flex: none; }
  .contact-band__address { margin-top: 14px; font-size: 17px; line-height: 22px; }

  .band-sweep {
    position: absolute; left: 0; top: 0; width: 736px; height: 424px;
    z-index: 1;
  }

  .world-map {
    position: absolute; left: 40px; top: 40px; width: 656px; height: 340px;
    background: radial-gradient(closest-side, var(--map-tone) 0%, rgba(61,58,59,0.55) 55%, rgba(34,31,32,0) 100%);
  }
  .card--back .wordmark {
    left: 0; right: 0; top: 180px; justify-content: center;
    font-size: 56px; font-weight: 400; color: #ffffff;
  }
  .card--back .wordmark__dot { width: 74px; height: 74px; }
  .tagline {
    position: absolute; left: 0; right: 0; top: 268px; text-align: center;
    font-family: "Arvo", serif; font-weight: 700; font-size: 29px; color: #ffffff;
  }
</style>
</head>
<body>
  <section class="card card--front">
    <div class="wordmark"><span class="wordmark__dot"></span>plumvexo</div>
    <div class="contact-band">
      <p class="contact-band__name">Martin Kessler</p>
      <p class="contact-band__role">Managing Director</p>
      <ul class="contact-list">
        <li>
          <svg viewBox="0 0 16 16" fill="currentColor" aria-hidden="true"><path d="M2 6c0-2 3-3 6-3s6 1 6 3v1h-3V5.5H5V7H2z"/><path d="M4 8h8l1 5H3z"/></svg>
          (+61) 7 5128 4409
        </li>
        <li>
          <svg viewBox="0 0 16 16" fill="none" stroke="currentColor" stroke-width="1.6" aria-hidden="true"><rect x="1.5" y="3.5" width="13" height="9"/><path d="M1.5 3.5 8 9l6.5-5.5"/></svg>
          hello@plumvexo.com
        </li>
        <li>
          <svg viewBox="0 0 16 16" fill="none" stroke="currentColor" stroke-width="1.3" aria-hidden="true"><circle cx="8" cy="8" r="6.5"/><ellipse cx="8" cy="8" rx="3" ry="6.5"/><path d="M1.5 8h13M2.5 4.8h11M2.5 11.2h11"/></svg>
          www.plumvexo.com
        </li>
      </ul>
      <p class="contact-band__address">PO Box 4172 Harlow St<br>Riverton City Country 4172</p>
    </div>
    <svg class="band-sweep" viewBox="0 0 736 424" aria-hidden="true">
      <defs>
        <linearGradient id="sweep-fill" x1="0" y1="0" x2="1" y2="1">
          <stop offset="0" stop-color="#e0393f"/>
          <stop offset="0.6" stop-color="#c42a3d"/>
          <stop offset="1" stop-color="#a4213b"/>
        </linearGradient>
      </defs>
      <circle cx="620" cy="330" r="190" fill="url(#sweep-fill)"/>
      <circle cx="620" cy="330" r="150" fill="none" stroke="#f1f1f1" stroke-width="3" opacity="0.9"/>
    </svg>
  </section>

  <section class="card card--back">
    <div class="world-map" role="img" aria-label="Dotted world map in soft grey"></div>
    <div class="wordmark"><span class="wordmark__dot"></span>plumvexo</div>
    <p class="tagline">Advertise anywhere, anytime!</p>
  </section>
</body>
</html>
```